BRV Online

We are a telemedicine based HIV treatment, prevention and hep c clinic looking to help make our online presence known.

Target Market(s)

Future patients. We want to this be informative and have stock images of all different types of people

Industry/Entity Type

Medical

Coding

Coded - Design and coding required

Requirements
Must have
• A Home Page, A page on PrEP, HIV treatment and Hep C. A box in the corner that says book now and a contact us page.

```html
<!DOCTYPE html>
<html lang="en">
<head>
<meta charset="utf-8">
<title>BRV Online — Online HIV &amp; Hepatitis C Care</title>
<link href="https://fonts.googleapis.com/css2?family=Merriweather:wght@700;900&family=Roboto:wght@400;500;700&display=swap" rel="stylesheet">
<style>
:root{
  --blue:#0a4fa3;
  --blue-deep:#0b3f8f;
  --blue-bright:#0a8fd0;
  --green:#5fb13a;
  --green-light:#8cc63f;
  --ink:#111111;
  --text:#444444;
  --grey-bg:#f5f5f5;
  --white:#ffffff;
  --footer:#111214;
}
*{box-sizing:border-box;margin:0;padding:0}
html,body{width:1200px;height:4260px;overflow:hidden}
body{position:relative;font-family:"Roboto",Arial,sans-serif;color:var(--text);background:var(--white)}
.abs{position:absolute}
.serif{font-family:"Merriweather",Georgia,serif}
.btn{position:absolute;display:flex;align-items:center;justify-content:center;border-radius:30px;color:#fff;font-weight:700;font-size:14px;letter-spacing:.2px;text-transform:uppercase;background:linear-gradient(90deg,var(--green),var(--green-light))}
.section-title{position:absolute;left:0;width:1200px;text-align:center;font-family:"Merriweather",Georgia,serif;font-weight:900;color:var(--ink);font-size:40px;letter-spacing:.5px}
.underline{position:absolute;left:565px;width:70px;height:3px;background:var(--blue)}

/* header */
.site-header{position:absolute;top:0;left:0;width:1200px;height:114px;background:#fff}
.brand{position:absolute;display:flex;align-items:center;gap:12px;font-family:"Roboto",sans-serif;font-weight:700;color:var(--blue-deep)}
.brand-dot{width:40px;height:40px;border-radius:50%;background:var(--green)}
.nav{position:absolute;top:46px;left:454px;display:flex;gap:28px;font-size:13px;font-weight:500;color:#222}
.nav .active{color:var(--blue);text-decoration:underline}

/* hero */
.hero-photo{position:absolute;top:114px;left:0;width:1200px;height:680px;background:linear-gradient(110deg,#6f6356 0%,#a69784 35%,#d8d0c4 65%,#b9b2a8 100%)}
.hero-shade{position:absolute;top:114px;left:0;width:760px;height:680px;background:linear-gradient(90deg,rgba(20,20,20,.55),rgba(20,20,20,0))}
.hero-title{left:144px;top:232px;width:560px;color:#fff;font-size:41px;line-height:48px;font-weight:700}
.hero-text{left:144px;top:386px;width:520px;color:#fff;font-size:19px;line-height:30px}
.dots{left:552px;top:644px;display:flex;gap:16px;align-items:center}
.dots span{width:9px;height:9px;border-radius:50%;background:#fff}
.dots .on{width:18px;height:18px;border:2px solid #fff;background:transparent;position:relative}

/* mission */
.mission{position:absolute;top:760px;left:0;width:1200px;height:424px;background:var(--grey-bg)}
.mission-text{left:140px;top:937px;width:920px;text-align:center;font-size:15.5px;line-height:25px;color:#333}

/* services */
.card{position:absolute;top:1389px;width:280px;height:350px;border-radius:16px;overflow:hidden}
.card-photo{position:absolute;inset:0}
.card-label{position:absolute;left:0;bottom:28px;width:100%;text-align:center;color:#fff;font-weight:700;font-size:16px}
.card-featured{background:linear-gradient(160deg,var(--green-light),var(--green))}
.card-featured h3{position:absolute;top:130px;width:100%;text-align:center;color:#fff;font-size:16px;font-weight:700}
.card-featured p{position:absolute;top:160px;left:24px;width:232px;text-align:center;color:#fff;font-size:14px;line-height:22.5px}
.learn{position:absolute;left:70px;top:262px;width:140px;height:40px;border-radius:22px;background:var(--blue);color:#fff;font-weight:700;font-size:13px;display:flex;align-items:center;justify-content:center}

/* trust */
.trust-title{color:#fff}
.feat{position:absolute;color:#fff;font-weight:700;font-size:14px;line-height:23px;text-transform:uppercase}
.ic{position:absolute;width:74px;height:74px;border-radius:50%;background:#fff;display:flex;align-items:center;justify-content:center}
.ic.green{background:var(--green)}

/* patient care */
.pc-title{left:625px;top:2870px;font-size:40px;line-height:50px;font-weight:900;color:var(--ink)}
.pc-text{left:625px;width:430px;font-size:14px;line-height:23px;text-align:justify;color:#555}

/* contact */
.contact{position:absolute;top:3381px;left:0;width:1200px;height:480px;background:var(--grey-bg)}
.field{position:absolute;left:210px;width:380px;height:46px;background:#fff;border-radius:24px;display:flex;align-items:center;font-size:13px;font-weight:500;color:#333;box-shadow:0 2px 8px rgba(0,0,0,.05)}
.field .fi{width:48px;display:flex;justify-content:center;border-right:1px solid #e4e4e4;height:26px;align-items:center;margin-right:14px}
.message{position:absolute;left:607px;top:3544px;width:383px;height:168px;background:#fff;border-radius:22px;box-shadow:0 2px 8px rgba(0,0,0,.05);font-size:13px;font-weight:500;color:#333}

/* footer */
.footer{position:absolute;top:3900px;left:0;width:1200px;height:360px;background:var(--footer)}
.f-head{position:absolute;top:4005px;color:#fff;font-size:13px;font-weight:700}
.f-head::after{content:"";position:absolute;left:0;top:22px;width:32px;height:2px;background:var(--green)}
.f-links{position:absolute;top:4045px;left:410px;color:#eee;font-size:12px;line-height:29.5px}
.f-info{position:absolute;left:550px;display:flex;align-items:flex-start;gap:14px;color:#eee;font-size:12px;line-height:17px}
.f-info .b{width:24px;height:24px;border-radius:50%;background:#2a2b2e;flex:none;display:flex;align-items:center;justify-content:center}
.newsletter{position:absolute;left:792px;top:4048px;width:263px;height:41px;background:#fff;border-radius:22px;display:flex;align-items:center;padding-left:16px;font-size:12px;color:#333}
.f-rule{position:absolute;left:144px;top:4198px;width:911px;height:1px;background:#2c2d30}
.copy{position:absolute;left:0;width:1200px;top:4220px;text-align:center;color:#ddd;font-size:11px}
.social{position:absolute;top:4214px;width:30px;height:30px;border-radius:50%;background:#2a2b2e}
</style>
</head>
<body>

<header class="site-header">
  <div class="brand" style="left:144px;top:33px;font-size:22px"><span class="brand-dot"></span>BRV Online</div>
  <nav class="nav">
    <span class="active">Home</span><span>PrEP</span><span>HIV Treatment</span><span>Hepatitis C (Hep C)</span><span>Contact Us</span>
  </nav>
  <div class="btn" style="left:936px;top:36px;width:119px;height:42px;font-size:13px">Book Now</div>
</header>

<div class="hero-photo" role="img" aria-label="Doctor holding a video consultation with an elderly patient on a tablet"></div>
<div class="hero-shade"></div>
<h1 class="abs serif hero-title">Compassionate Online HIV &amp; Hepatitis C Care</h1>
<p class="abs hero-text">Access confidential, professional telemedicine services for HIV treatment, PrEP, and Hepatitis C care—all from the comfort of your home.</p>
<div class="btn" style="left:144px;top:496px;width:215px;height:41px">Book An Appointment</div>
<div class="abs dots"><span></span><span class="on"></span><span></span><span></span></div>

<div class="mission"></div>
<svg class="abs" style="left:0;top:640px" width="1200" height="160" viewBox="0 0 1200 160">
  <path d="M0 120 C250 20 450 30 620 80 C820 140 980 110 1200 30 L1200 0 L0 0Z" fill="none"/>
  <path d="M0 120 C250 20 450 30 620 80 C820 140 980 110 1200 30 L1200 60 C1000 150 820 170 620 120 C430 70 250 80 0 140Z" fill="#0a5fb0"/>
  <path d="M0 120 C250 20 450 30 620 80 C820 140 980 110 1200 30 L1200 160 L0 160Z" fill="#f5f5f5"/>
  <path d="M620 105 C820 165 1000 140 1200 50 L1200 62 C1000 155 820 172 620 118Z" fill="#0a8fd0"/>
</svg>

<h2 class="section-title" style="top:862px">OUR MISSION</h2>
<div class="underline" style="top:910px"></div>
<p class="abs mission-text">BRV Online is committed to providing accessible, compassionate, and evidence-based telemedicine services for HIV prevention, HIV treatment, and Hepatitis C care. Our mission is to eliminate barriers to quality healthcare by delivering confidential, personalized medical support that empowers individuals to take control of their health, improve their well-being, and build healthier communities.</p>
<div class="btn" style="left:493px;top:1060px;width:215px;height:39px">Book An Appointment</div>

<h2 class="section-title" style="top:1298px">SERVICES OFFERED</h2>
<div class="underline" style="top:1348px"></div>

<div class="card" style="left:144px">
  <div class="card-photo" role="img" aria-label="Caregiver holding an elderly patient's hands" style="background:linear-gradient(160deg,#a9c4d6,#7d98ad 55%,#4e5d6a)"></div>
  <div class="card-label">HIV TREATMENT</div>
</div>
<div class="card card-featured" style="left:460px">
  <svg class="abs" style="left:102px;top:42px" width="76" height="76" viewBox="0 0 76 76">
    <circle cx="38" cy="38" r="38" fill="#fff"/>
    <path d="M38 20 L52 26 V38 C52 47 46 53 38 56 C30 53 24 47 24 38 V26Z" fill="none" stroke="#0a4fa3" stroke-width="2"/>
    <path d="M38 31 V45 M31 38 H45" stroke="#5fb13a" stroke-width="3"/>
  </svg>
  <h3>PREP PREVENTION</h3>
  <p>Protect yourself against HIV with convenient online PrEP consultations, prescriptions, and regular follow-up care.</p>
  <div class="learn">LEARN MORE</div>
</div>
<div class="card" style="left:775px">
  <div class="card-photo" role="img" aria-label="Doctor holding a rendered liver surrounded by virus particles" style="background:radial-gradient(circle at 55% 50%,#b06a45 0,#6a4a52 25%,#4a6a88 60%,#2e4a66 100%)"></div>
  <div class="card-label">HEPATITIS C CARE</div>
</div>

<!-- trust band -->
<svg class="abs" style="left:0;top:1830px" width="1200" height="880" viewBox="0 0 1200 880">
  <defs>
    <linearGradient id="trustBg" x1="0" y1="1" x2="1" y2="0">
      <stop offset="0" stop-color="#0b3f8f"/><stop offset=".5" stop-color="#0a5fb0"/><stop offset="1" stop-color="#0a93d2"/>
    </linearGradient>
  </defs>
  <path d="M0 38 C200 140 400 150 640 80 C850 20 1030 -10 1200 40 L1200 880 L0 880Z" fill="#8cc63f"/>
  <path d="M0 38 C200 160 420 170 650 100 C860 40 1040 30 1200 70 L1200 880 L0 880Z" fill="url(#trustBg)"/>
  <circle cx="598" cy="509" r="188" fill="none" stroke="#fff" stroke-width="2"/>
  <circle cx="598" cy="509" r="176" fill="none" stroke="#fff" stroke-width="1" opacity=".6"/>
  <circle cx="598" cy="509" r="154" fill="#fff"/>
  <g fill="#fff"><circle cx="476" cy="364" r="5"/><circle cx="722" cy="364" r="5"/><circle cx="412" cy="509" r="5"/><circle cx="786" cy="509" r="5"/><circle cx="484" cy="655" r="5"/><circle cx="715" cy="655" r="5"/><circle cx="598" cy="697" r="5"/></g>
</svg>
<h2 class="section-title trust-title" style="top:2030px">WHY PATIENTS TRUST US</h2>
<div class="underline" style="top:2080px;background:#fff"></div>
<div class="brand" style="left:480px;top:2318px;font-size:26px"><span class="brand-dot" style="width:36px;height:36px"></span>BRV Online</div>

<div class="feat" style="left:160px;top:2143px;width:222px;text-align:right">Experienced Medical<br>Providers</div>
<div class="ic" style="left:396px;top:2129px"><svg width="36" height="36" viewBox="0 0 36 36" fill="none" stroke="#0a4fa3" stroke-width="2"><circle cx="18" cy="11" r="6"/><path d="M6 33 C6 24 11 20 18 20 C25 20 30 24 30 33Z"/><path d="M18 22 V30 M14 26 H22" stroke="#5fb13a"/></svg></div>

<div class="ic" style="left:730px;top:2129px"><svg width="38" height="36" viewBox="0 0 38 36" fill="none" stroke="#0a4fa3" stroke-width="2"><circle cx="19" cy="8" r="5"/><circle cx="9" cy="18" r="4"/><circle cx="29" cy="18" r="4"/><path d="M2 32 C2 26 5 24 9 24 C13 24 16 26 16 32 M22 32 C22 26 25 24 29 24 C33 24 36 26 36 32"/></svg></div>
<div class="feat" style="left:818px;top:2143px;width:220px">Compassionate Patient<br>Support</div>

<div class="feat" style="left:150px;top:2316px;width:158px;text-align:right">Confidential<br>&amp; Secure Care</div>
<div class="ic green" style="left:323px;top:2302px"><svg width="36" height="36" viewBox="0 0 36 36" fill="none" stroke="#fff" stroke-width="2"><path d="M18 3 L29 8 V17 C29 24 24 28 18 31 C12 28 7 24 7 17 V8Z"/><path d="M18 11 V21 M13 16 H23"/></svg></div>

<div class="ic" style="left:803px;top:2302px"><svg width="38" height="34" viewBox="0 0 38 34" fill="none" stroke="#0a4fa3" stroke-width="2"><rect x="3" y="3" width="32" height="22" rx="2"/><path d="M13 31 H25 M19 25 V31"/><path d="M19 9 V19 M14 14 H24" stroke="#5fb13a"/></svg></div>
<div class="feat" style="left:891px;top:2316px;width:200px">HIPAA-Compliant<br>Telemedicine</div>

<div class="feat" style="left:220px;top:2503px;width:184px;text-align:right">Convenient Online<br>Appointments</div>
<div class="ic" style="left:414px;top:2489px"><svg width="36" height="36" viewBox="0 0 36 36" fill="none" stroke="#0a4fa3" stroke-width="2"><rect x="4" y="6" width="26" height="24" rx="2"/><path d="M4 13 H30 M11 3 V9 M23 3 V9"/><circle cx="27" cy="27" r="6" fill="#fff"/><path d="M24 27 L26 29 L30 25" stroke="#5fb13a"/></svg></div>

<div class="ic" style="left:710px;top:2489px"><svg width="36" height="36" viewBox="0 0 36 36" fill="none" stroke="#0a4fa3" stroke-width="2"><circle cx="22" cy="11" r="7"/><path d="M22 7 V15" stroke="#5fb13a"/><path d="M3 30 H10 V22 H3Z M10 24 C15 22 18 22 22 25 L30 22 C32 22 33 24 31 26 L22 31 H10"/></svg></div>
<div class="feat" style="left:796px;top:2503px;width:220px">Affordable Healthcare<br>Solutions</div>

<div class="ic" style="left:561px;top:2542px"><svg width="34" height="36" viewBox="0 0 34 36" fill="none" stroke="#0a4fa3" stroke-width="2"><rect x="5" y="5" width="22" height="28" rx="2"/><path d="M11 3 H21 V8 H11Z M10 15 H22 M10 21 H18 M10 27 H16"/><circle cx="25" cy="27" r="5" stroke="#5fb13a"/></svg></div>
<div class="feat" style="left:400px;top:2629px;width:396px;text-align:center">Personalized Treatment Plans</div>

<!-- patient-centered care -->
<div class="abs" style="left:145px;top:2810px;width:172px;height:172px;border-radius:50%;background:#e6e9ee"></div>
<svg class="abs" style="left:140px;top:2854px" width="432" height="432" viewBox="0 0 432 432">
  <defs><linearGradient id="ring" x1="0" y1="0" x2="1" y2="1"><stop offset="0" stop-color="#0a93d2"/><stop offset="1" stop-color="#0b3f8f"/></linearGradient></defs>
  <path d="M216 6 A210 210 0 1 1 6 216" fill="none" stroke="url(#ring)" stroke-width="8"/>
</svg>
<div class="abs" role="img" aria-label="Smiling patient in a head scarf comforted by a caregiver" style="left:145px;top:2859px;width:400px;height:400px;border-radius:50%;background:radial-gradient(circle at 55% 40%,#e4d3c4 0,#c9b8a6 45%,#9aa7b2 100%)"></div>

<h2 class="abs serif pc-title">PATIENT-<br>CENTERED CARE</h2>
<p class="abs pc-text" style="top:2985px">We believe healthcare should be accessible, respectful, and judgment-free. Our mission is to provide high-quality telemedicine services that empower individuals to take control of their health with confidence and privacy.</p>
<p class="abs pc-text" style="top:3087px">Sed ut perspiciatis unde omnis iste natus error sit voluptatem accusantium doloremque laudantium, totam rem aperiam, eaque ipsa quae ab illo inventore veritatis et quasi architecto beatae vitae dicta sunt explicabo. Nemo enim ipsam voluptatem quia voluptas sit aspernatur aut odit aut fugitea.</p>
<div class="btn" style="left:625px;top:3232px;width:124px;height:40px">Book Now</div>

<!-- contact -->
<div class="contact"></div>
<h2 class="section-title" style="top:3450px">CONTACT US</h2>
<div class="underline" style="top:3500px"></div>
<div class="field" style="top:3544px"><span class="fi"><svg width="12" height="13" viewBox="0 0 12 13" fill="#0a4fa3"><circle cx="6" cy="3.5" r="3.2"/><path d="M0 13 C0 8.5 2.5 7 6 7 C9.5 7 12 8.5 12 13Z"/></svg></span>Your Name</div>
<div class="field" style="top:3605px"><span class="fi"><svg width="12" height="12" viewBox="0 0 12 12" fill="#0a4fa3"><path d="M2 0 L4.5 3 L3 4.5 C4 6.5 5.5 8 7.5 9 L9 7.5 L12 10 L10 12 C5 11.5 0.5 7 0 2Z"/></svg></span>Email</div>
<div class="field" style="top:3666px"><span class="fi"><svg width="13" height="10" viewBox="0 0 13 10" fill="#0a4fa3"><rect width="13" height="10" rx="1"/><path d="M0.5 1 L6.5 6 L12.5 1" stroke="#fff" fill="none"/></svg></span>Phone</div>
<div class="message"><div style="position:absolute;left:20px;top:22px;display:flex;align-items:center"><svg width="16" height="12" viewBox="0 0 16 12" fill="#0a4fa3"><ellipse cx="6" cy="5" rx="6" ry="4.5"/><ellipse cx="11" cy="7" rx="5" ry="4"/></svg><span style="border-left:1px solid #e4e4e4;height:26px;margin:0 14px"></span><span>Your Message</span></div></div>
<div class="btn" style="left:522px;top:3739px;width:156px;height:41px">Send Message</div>

<!-- footer -->
<svg class="abs" style="left:0;top:3800px" width="1200" height="110" viewBox="0 0 1200 110">
  <path d="M0 130 C200 20 380 0 560 40 C760 90 980 90 1200 0 L1200 110 L0 110Z" fill="#0b3f8f"/>
  <path d="M0 130 C220 45 400 30 580 62 C780 100 990 110 1200 40 L1200 110 L0 110Z" fill="#0a8fd0"/>
  <path d="M0 130 C230 60 410 50 590 80 C790 112 1000 125 1200 70 L1200 110 L0 110Z" fill="#111214"/>
</svg>
<div class="footer"></div>
<div class="brand" style="left:144px;top:4082px;font-size:20px;color:#fff"><span class="brand-dot" style="width:34px;height:34px"></span>BRV Online</div>

<div class="f-head" style="left:410px">QUICK LINKS</div>
<div class="f-links">Home<br>PrEP<br>HIV Treatment<br>Hepatitis C (Hep C)<br>Contact Us</div>

<div class="f-head" style="left:550px">CONTACT INFO</div>
<div class="f-info" style="top:4047px"><span class="b"><svg width="10" height="10" viewBox="0 0 12 12" fill="#5fb13a"><path d="M2 0 L4.5 3 L3 4.5 C4 6.5 5.5 8 7.5 9 L9 7.5 L12 10 L10 12 C5 11.5 0.5 7 0 2Z"/></svg></span><span style="padding-top:4px">+1 (555) 014 2290</span></div>
<div class="f-info" style="top:4089px"><span class="b"><svg width="11" height="8" viewBox="0 0 13 10" fill="#5fb13a"><rect width="13" height="10" rx="1"/></svg></span><span style="padding-top:4px">info@brvonline.com</span></div>
<div class="f-info" style="top:4131px"><span class="b"><svg width="9" height="12" viewBox="0 0 10 14" fill="#5fb13a"><path d="M5 0 C8 0 10 2 10 5 C10 8 5 14 5 14 C5 14 0 8 0 5 C0 2 2 0 5 0Z"/></svg></span><span style="padding-top:2px">465, Lorum Ipsum Dolore Sed,<br>United States</span></div>

<div class="f-head" style="left:792px">NEWSLETTER</div>
<div class="newsletter">Email Address<svg style="position:absolute;right:16px" width="16" height="14" viewBox="0 0 16 14" fill="#5fb13a"><path d="M0 6 L16 0 L12 14 L8 9 Z"/></svg></div>

<div class="f-rule"></div>
<div class="copy">© 2026 &nbsp;/ &nbsp; All Rights Reserved</div>
<span class="social" style="left:945px"></span>
<span class="social" style="left:985px;background:var(--green)"></span>
<span class="social" style="left:1023px"></span>

</body>
</html>
```